Website re-design for Ferncrest LLC website ( has existing website )

Looking to do a complete re-design of Ferncrestllc. The existing website is dated and built in wordpress. The new website will not be wordpress. The project folder includes an overview.txt file with details on the project. The file also contains a list of websites that he/she likes which I am sure is very helpful .
Number of Pages Required
1 page

```html
<!DOCTYPE html>
<html lang="en">
<head>
<meta charset="utf-8">
<title>Ferncrest – Lake Weed Removal</title>
<link href="https://fonts.googleapis.com/css2?family=Montserrat:ital,wght@0,400;0,500;0,600;0,700;1,800&family=Open+Sans:wght@400;600;700&display=swap" rel="stylesheet">
<style>
:root{
  --bg:#c8d9e5;
  --card:#dde7ee;
  --blue:#1d5fb0;
  --blue-dark:#164c8f;
  --heading-blue:#2a6cc0;
  --ink:#2a2f36;
  --nav-ink:#1b2530;
  --muted:#4b5560;
  --footer:#222325;
  --footer-2:#2c2d30;
  --white:#ffffff;
}
*{box-sizing:border-box;margin:0;padding:0}
html,body{width:1200px;height:4724px;overflow:hidden}
body{background:var(--bg);font-family:"Montserrat",sans-serif;color:var(--ink)}
.page{position:relative;width:1200px;height:4724px;overflow:hidden;background:var(--bg)}

/* hero */
.hero-photo{position:absolute;left:0;top:0;width:1200px;height:890px;
  background:linear-gradient(180deg,#e4f0f4 0%,#cfe2ea 14%,#6c8f7a 28%,#3d6353 40%,#42685a 50%,#7c9aa0 60%,#94acb4 74%,#adc2ce 86%,var(--bg) 100%)}
.brand{position:absolute;display:flex;align-items:center;gap:12px}
.brand-mark{width:16px;height:16px;background:var(--blue)}
.brand-name{font-family:"Montserrat",sans-serif;font-size:32px;font-weight:600;line-height:1;color:var(--nav-ink);letter-spacing:.5px}
.brand.on-dark .brand-name{color:var(--white)}
.top-contact{position:absolute;top:30px;display:flex;align-items:center;gap:10px;font-size:12px;color:var(--nav-ink)}
.top-contact .ic{width:24px;height:24px;border-radius:50%;background:#fff;display:flex;align-items:center;justify-content:center}
.top-contact small{display:block;color:var(--blue);font-size:10px}
.quote-btn{position:absolute;left:971px;top:30px;width:137px;height:33px;background:var(--blue);color:#fff;font-size:12px;display:flex;align-items:center;justify-content:center;gap:8px}
.quote-btn i{width:16px;height:16px;border-radius:50%;background:#fff;display:inline-block}
.nav{position:absolute;top:82px;left:528px;font-size:13px;letter-spacing:1px;color:var(--nav-ink)}
.nav a{color:inherit;text-decoration:none;position:absolute;white-space:nowrap}
.nav .active{color:var(--blue);border-bottom:2px solid var(--blue);padding-bottom:5px}
.hero-kicker{position:absolute;top:480px;left:0;width:1200px;text-align:center;font-size:21px;color:#fff;letter-spacing:1px}
.hero-title{position:absolute;top:513px;left:0;width:1200px;text-align:center;font-size:56px;font-weight:800;font-style:italic;color:#fff;letter-spacing:1px}
.slider-dots{position:absolute;left:1130px;top:420px;display:flex;flex-direction:column;gap:14px}
.slider-dots span{display:flex;align-items:center;gap:6px;font-size:8px;color:#fff}
.slider-dots span::after{content:"";width:5px;height:5px;border-radius:50%;background:#fff}

/* section headings */
.sec-title{position:absolute;left:0;width:1200px;text-align:center;font-family:"Open Sans",sans-serif;font-weight:600;font-size:30px;letter-spacing:1px;color:#1f2328}
.sec-sub{position:absolute;left:0;width:1200px;text-align:center;font-size:13px;line-height:17px;color:#2d333a}

/* about */
.about-photo{position:absolute;left:150px;top:944px;width:460px;height:455px;border-radius:48% 52% 44% 56%/50% 46% 54% 50%;
  background:radial-gradient(ellipse at 50% 45%,#56646c 0%,#3b464d 30%,#b9c6ce 60%,#e6edf1 72%,var(--bg) 85%)}
.about-col{position:absolute;left:651px;width:475px}
.about-col h3{font-family:"Open Sans",sans-serif;font-weight:600;font-size:19px;color:var(--heading-blue);letter-spacing:1.5px;border-bottom:2px solid var(--heading-blue);display:inline-block;padding-bottom:2px;margin-bottom:10px}
.about-col p{font-size:13.4px;line-height:26.3px;color:#3a424b}
.btn{position:absolute;background:var(--blue);color:#fff;font-size:13px;display:flex;align-items:center;justify-content:center;box-shadow:0 2px 3px rgba(0,0,0,.25)}

/* service cards */
.svc{position:absolute;top:1586px;width:250px;height:386px;background:var(--card);box-shadow:0 3px 6px rgba(0,0,0,.12)}
.svc .ph{position:absolute;left:10px;top:0;width:230px;height:190px}
.svc .badge{position:absolute;left:104px;top:168px;width:42px;height:42px;border-radius:50%;background:var(--card);display:flex;align-items:center;justify-content:center}
.svc h4{position:absolute;top:222px;left:10px;right:10px;text-align:center;font-family:"Open Sans",sans-serif;font-weight:600;font-size:15px;line-height:18px;letter-spacing:1.2px;color:#1f2328}
.svc p{position:absolute;top:268px;left:20px;right:20px;text-align:center;font-size:12.5px;line-height:18px;color:#3b434b}
.svc .go{position:absolute;left:113px;top:336px;width:24px;height:24px;border-radius:50%;background:var(--blue);display:flex;align-items:center;justify-content:center}

/* testimonials */
.testi-band{position:absolute;left:0;top:2096px;width:1200px;height:551px;
  background:linear-gradient(180deg,#3b4c53 0%,#2e4640 30%,#234036 55%,#1f3b41 80%,#2b4c5c 100%)}
.testi-title{top:2180px;color:#fff}
.quote-mark{position:absolute;left:0;top:2230px;width:1200px;text-align:center;font-family:"Open Sans",sans-serif;font-size:86px;font-weight:700;color:#fff;line-height:1}
.testi-text{position:absolute;left:320px;top:2302px;width:560px;text-align:center;font-size:13px;line-height:17px;color:#fff}
.testi-author{position:absolute;left:0;top:2370px;width:1200px;text-align:center;font-size:13px;font-weight:700;color:#fff}
.ba-frame{position:absolute;left:95px;top:2436px;width:1013px;height:372px;background:var(--card)}
.ba-before{position:absolute;left:117px;top:2458px;width:535px;height:350px;clip-path:polygon(0 0,100% 0,88% 100%,0 100%);
  background:linear-gradient(180deg,#6f9a5a 0%,#4e7a3f 35%,#8a8f7c 60%,#6d6a58 100%)}
.ba-after{position:absolute;left:548px;top:2458px;width:538px;height:350px;clip-path:polygon(12% 0,100% 0,100% 100%,0 100%);
  background:linear-gradient(180deg,#d9e8ef 0%,#7a9a55 30%,#607f3e 55%,#a79c83 80%,#8b8270 100%)}
.ba-label{position:absolute;top:2788px;width:140px;height:42px;background:var(--blue);color:#fff;font-weight:800;font-style:italic;font-size:18px;letter-spacing:2px;display:flex;align-items:center;justify-content:center;clip-path:polygon(10% 0,100% 0,90% 100%,0 100%)}
.ba-arrow{position:absolute;top:2627px;width:30px;height:30px;border-radius:50%;display:flex;align-items:center;justify-content:center;border:2px solid #fff}

/* feature grid */
.feat{position:absolute;width:315px;background:var(--card)}
.feat.hot{background:var(--blue);color:#fff}
.feat .ico{position:absolute;left:18px;top:38px;width:78px;height:78px}
.feat h4{position:absolute;left:104px;top:52px;font-family:"Montserrat",sans-serif;font-weight:500;font-size:17px;line-height:22px;letter-spacing:.5px}
.feat p{position:absolute;left:18px;right:22px;top:134px;font-size:13px;line-height:18px;color:#4b5560}
.feat.hot p{color:#fff}
.feat.row2 p{top:148px}

/* faq */
.faq-title{position:absolute;left:88px;top:3624px;font-family:"Open Sans",sans-serif;font-weight:600;font-size:30px;letter-spacing:1.5px;color:#3a3f45;border-bottom:2px solid var(--heading-blue);padding-bottom:2px}
.faq-item{position:absolute;left:73px;width:542px;background:var(--card);padding:0 20px;font-size:12.5px;color:#2d333a;display:flex;align-items:center;justify-content:space-between;height:33px}
.faq-item.open{height:105px;align-items:flex-start;flex-direction:column;justify-content:flex-start;padding-top:11px}
.faq-item.open p{font-size:11.5px;line-height:14px;color:#555e68;margin-top:9px;width:420px}
.faq-item .chev{width:22px;height:22px;border-radius:50%;background:var(--blue);display:flex;align-items:center;justify-content:center;flex:none}
.faq-item.open .chev{position:absolute;right:10px;top:9px}
.pager{position:absolute;left:75px;top:4062px;display:flex;gap:11px}
.pager span{width:34px;height:34px;display:flex;align-items:center;justify-content:center;font-size:12px;color:#2d333a}
.pager .on{background:var(--blue);color:#fff}
.faq-photo{position:absolute;left:664px;top:3632px;width:458px;height:458px;border-radius:50%;
  background:linear-gradient(180deg,#4e86d4 0%,#8cb6e6 35%,#2c5a9a 55%,#3f6fa5 75%,#24456e 100%)}

/* footer */
.footer-wave{position:absolute;left:0;top:4260px}
.footer{position:absolute;left:0;top:4330px;width:1200px;height:394px;background:var(--footer)}
.follow{position:absolute;left:188px;top:4510px;font-family:"Open Sans",sans-serif;font-weight:600;font-size:18px;color:#fff}
.socials{position:absolute;left:166px;top:4545px;display:flex;gap:11px}
.socials span{width:28px;height:28px;border-radius:50%;background:#fff}
.socials span:first-child{background:var(--blue)}
.f-head{position:absolute;font-family:"Open Sans",sans-serif;font-weight:600;font-size:19px;color:#fff}
.f-head::after{content:"";display:block;width:48px;height:2px;background:#fff;margin-top:10px}
.f-links{position:absolute;left:405px;top:4468px;list-style:none;font-size:12.5px;letter-spacing:1.2px;color:#fff;line-height:25px}
.f-links li::before{content:">";margin-right:12px}
.f-info{position:absolute;left:552px;font-size:12.5px;line-height:25px;color:#fff;display:flex;gap:14px}
.f-info svg{margin-top:5px;flex:none}
.field{position:absolute;background:#e9edf1;border:1px solid #cfd6dc;font-size:11px;color:#6c747c;padding:8px 10px}
.submit{position:absolute;left:756px;top:4546px;width:137px;height:33px;background:var(--blue);color:#fff;font-size:13px;font-style:italic;display:flex;align-items:center;justify-content:center}
.copy{position:absolute;left:0;top:4680px;width:1200px;height:44px;background:var(--footer-2);text-align:center;font-size:12px;line-height:44px;color:#c9ccd0}
.copy b{color:var(--heading-blue);font-weight:500}
</style>
</head>
<body>
<div class="page">

  <!-- hero -->
  <div class="hero-photo" role="img" aria-label="Mountain lake with pine forested shoreline reflected in calm water"></div>
  <div class="brand" style="left:72px;top:52px">
    <span class="brand-mark"></span>
    <span class="brand-name">Ferncrest</span>
  </div>
  <div class="top-contact" style="left:625px">
    <span class="ic"><svg width="12" height="12" viewBox="0 0 24 24"><path fill="#1d5fb0" d="M6.6 10.8a15 15 0 006.6 6.6l2.2-2.2c.3-.3.7-.4 1-.2 1.1.4 2.3.6 3.6.6.6 0 1 .4 1 1V20c0 .6-.4 1-1 1A17 17 0 013 4c0-.6.4-1 1-1h3.5c.6 0 1 .4 1 1 0 1.3.2 2.5.6 3.6.1.3 0 .7-.2 1z"/></svg></span>
    <div><small>Call Us</small>(555) 014-2290</div>
  </div>
  <div class="top-contact" style="left:784px">
    <span class="ic"><svg width="12" height="12" viewBox="0 0 24 24"><path fill="#1d5fb0" d="M2 5h20v14H2z"/><path fill="none" stroke="#fff" stroke-width="2" d="M2 5l10 8 10-8"/></svg></span>
    <div><small>Email us</small>info@ferncrestllc.com</div>
  </div>
  <div class="quote-btn">Get A Quote <i></i></div>
  <nav class="nav">
    <a class="active" style="left:0">Home</a>
    <a style="left:107px">About Us</a>
    <a style="left:238px">Services ∨</a>
    <a style="left:362px">FAQs</a>
    <a style="left:462px">Contact Us</a>
    <a style="left:570px"><svg width="12" height="12" viewBox="0 0 24 24"><circle cx="10" cy="10" r="7" fill="none" stroke="#1b2530" stroke-width="2.5"/><path d="M15 15l6 6" stroke="#1b2530" stroke-width="2.5"/></svg></a>
  </nav>
  <div class="hero-kicker">Specializing In Residential &amp; Commercial</div>
  <h1 class="hero-title">LAKE WEED REMOVAL</h1>
  <div class="slider-dots"><span>01</span><span>02</span><span>03</span><span>04</span><span>05</span></div>

  <!-- about -->
  <h2 class="sec-title" style="top:866px">About Us</h2>
  <div class="about-photo" role="img" aria-label="Diver in wetsuit holding an armful of harvested lake weeds"></div>
  <div class="about-col" style="top:955px">
    <h3>Our Mission</h3>
    <p>Ferncrest LLC is a company formed in response to the increase in invasive species in Minnesota lakes and waterways. The impact of these fast-growing nuisances inspired our venture to effectively control unwanted lake weeds and create an enjoyable environment craved by waterfront property homeowners.</p>
  </div>
  <div class="about-col" style="top:1146px">
    <h3>Preserving the Good</h3>
    <p>We have partnered with The Compost Yard to recycle 100% of the lake weeds we remove. The types of materials used in compost have a huge impact on how long it takes to break down and how nutrient rich the end product will be. The lake weeds we provide have high levels of moisture as well as critically needed nitrogen. They are a great addition for making high quality compost.</p>
  </div>
  <div class="btn" style="left:651px;top:1357px;width:136px;height:33px">Read More</div>

  <!-- services -->
  <h2 class="sec-title" style="top:1478px">Service</h2>
  <p class="sec-sub" style="top:1523px">We know there is no life like the lake life and we are<br>dedicated to keeping it that way.</p>

  <div class="svc" style="left:64px">
    <div class="ph" role="img" aria-label="Gloved hands pulling submerged weeds from the water" style="background:linear-gradient(160deg,#6d9a3f,#3f6a2c 50%,#8d6b3a)"></div>
    <div class="badge"><svg width="24" height="24" viewBox="0 0 24 24"><circle cx="12" cy="12" r="9" fill="none" stroke="#1d5fb0" stroke-width="2.4"/></svg></div>
    <h4>Lake Weed Removal<br>(Submerged)</h4>
    <p>Reclaim open water in front of your dock, beach, or boat slip!</p>
    <div class="go"><svg width="10" height="10" viewBox="0 0 10 10"><path d="M3 1l4 4-4 4" fill="none" stroke="#fff" stroke-width="2"/></svg></div>
  </div>
  <div class="svc" style="left:336px">
    <div class="ph" role="img" aria-label="Divers working in shallow water along a wooded shore" style="background:linear-gradient(180deg,#9ab07a,#4e5e48 45%,#2f3a36)"></div>
    <div class="badge"><svg width="24" height="24" viewBox="0 0 24 24"><circle cx="12" cy="12" r="9" fill="none" stroke="#1d5fb0" stroke-width="2.4"/></svg></div>
    <h4>Zebra Mussel<br>Removal</h4>
    <p>This Invasive species is becoming an increasing risk to Minnesota waterways...</p>
    <div class="go"><svg width="10" height="10" viewBox="0 0 10 10"><path d="M3 1l4 4-4 4" fill="none" stroke="#fff" stroke-width="2"/></svg></div>
  </div>
  <div class="svc" style="left:611px">
    <div class="ph" role="img" aria-label="Rocky shoreline with clear turquoise water" style="background:linear-gradient(180deg,#cfe6f2,#6fc3c9 45%,#b6a88f 75%,#8a8476)"></div>
    <div class="badge"><svg width="24" height="24" viewBox="0 0 24 24"><circle cx="12" cy="12" r="9" fill="none" stroke="#1d5fb0" stroke-width="2.4"/></svg></div>
    <h4>Shoreline<br>Cleanups</h4>
    <p>Waves constantly litter trash, lake weeds, and other debris along your shoreline.</p>
    <div class="go"><svg width="10" height="10" viewBox="0 0 10 10"><path d="M3 1l4 4-4 4" fill="none" stroke="#fff" stroke-width="2"/></svg></div>
  </div>
  <div class="svc" style="left:884px">
    <div class="ph" role="img" aria-label="Loader moving a pile of rocks near the beach" style="background:linear-gradient(180deg,#c9d3d4,#5a6a4b 40%,#9c9486 75%,#7c766e)"></div>
    <div class="badge"><svg width="24" height="24" viewBox="0 0 24 24"><circle cx="12" cy="12" r="9" fill="none" stroke="#1d5fb0" stroke-width="2.4"/></svg></div>
    <h4 style="top:234px">Beach Sanding</h4>
    <p>Continuous waves wash away sand from your beach to expose mud and larger rocks...</p>
    <div class="go"><svg width="10" height="10" viewBox="0 0 10 10"><path d="M3 1l4 4-4 4" fill="none" stroke="#fff" stroke-width="2"/></svg></div>
  </div>
  <div class="btn" style="left:532px;top:2014px;width:136px;height:33px">View More</div>

  <!-- testimonials -->
  <div class="testi-band" role="img" aria-label="Forested mountain valley around a lake"></div>
  <h2 class="sec-title testi-title">Testimonials</h2>
  <div class="quote-mark">“</div>
  <p class="testi-text">Everyone used to jump off the water trampoline and instantly get tangled in lake weeds. We contacted Ferncrest and their SCUBA divers have now been solving our problem for the past 4 years!"</p>
  <p class="testi-author">– Willow Bay Shores Association (Lake Minnetonka)</p>
  <div class="ba-frame"></div>
  <div class="ba-before" role="img" aria-label="Wooden dock covered in tangled lake weeds before cleanup"></div>
  <div class="ba-after" role="img" aria-label="Same wooden dock clean after cleanup"></div>
  <div class="ba-label" style="left:266px">BEFORE</div>
  <div class="ba-label" style="left:760px">AFTER</div>
  <div class="ba-arrow" style="left:101px;background:#333"><svg width="10" height="10" viewBox="0 0 10 10"><path d="M7 1L3 5l4 4" fill="none" stroke="#fff" stroke-width="2"/></svg></div>
  <div class="ba-arrow" style="left:1070px;background:var(--blue)"><svg width="10" height="10" viewBox="0 0 10 10"><path d="M3 1l4 4-4 4" fill="none" stroke="#fff" stroke-width="2"/></svg></div>

  <!-- features -->
  <div class="feat" style="left:105px;top:2925px;height:294px">
    <svg class="ico" viewBox="0 0 78 78"><circle cx="39" cy="39" r="26" fill="none" stroke="#1d5fb0" stroke-width="5"/><circle cx="39" cy="39" r="7" fill="#1d5fb0"/></svg>
    <h4 style="color:#1f2328">Dangerous<br>Object Cleanups</h4>
    <p>Broken bottles, cans, sticks, and sharp rocks are some examples of underwater nuisances that keep you from fully enjoying your waterfront property. Our SCUBA divers comb through and clear away these objects in the treatment area that you choose.</p>
  </div>
  <div class="feat hot" style="left:444px;top:2925px;height:294px">
    <svg class="ico" viewBox="0 0 78 78"><circle cx="44" cy="18" r="8" fill="#fff"/><path d="M34 30h20l-4 24h-12z" fill="#fff"/><path d="M30 40L10 66" stroke="#fff" stroke-width="4"/></svg>
    <h4>Emergent Weed<br>Removal</h4>
    <p>Cattails, bulrushes, and other emergent plants can engulf your shoreline and make it impossible to put in a dock system. Clear a path out to open water with this service. (Department of Natural Resources permit may apply).</p>
  </div>
  <div class="feat" style="left:780px;top:2925px;height:294px">
    <svg class="ico" viewBox="0 0 78 78"><path d="M20 70C10 50 24 30 30 10c4 16 8 20 10 32 4-10 10-14 14-22 4 20 10 32 4 50z" fill="#1d5fb0"/></svg>
    <h4 style="color:#1f2328">Lake Weed Removal<br>(Floating)</h4>
    <p>Patches of floating weeds can drift in and stay in front of your shoreline. Clean this up on a recurring or per-time basis with this service.</p>
  </div>
  <div class="feat row2" style="left:105px;top:3239px;height:292px">
    <svg class="ico" viewBox="0 0 78 78"><circle cx="44" cy="42" r="24" fill="none" stroke="#1d5fb0" stroke-width="4"/><path d="M44 42V28M38 12h12M4 36h14M8 46h12M12 56h10" stroke="#1d5fb0" stroke-width="4"/></svg>
    <h4 style="color:#1f2328">Lost Item<br>Search</h4>
    <p>Have you dropped something of value in the water? From boat keys to tools to other items, our scuba divers scour the bottom to recover your belongings.</p>
  </div>
  <div class="feat row2" style="left:444px;top:3239px;height:292px">
    <svg class="ico" viewBox="0 0 78 78"><circle cx="26" cy="44" r="7" fill="#1d5fb0"/><path d="M30 50l18-22 14 6M24 54l-8 16M40 40l22-24" stroke="#1d5fb0" stroke-width="6" fill="none"/></svg>
    <h4 style="color:#1f2328">Selective<br>Harvesting</h4>
    <p>Our dive team has the ability to leave comb through sections and specifically target invasive plant species, leaving all native plant species intact. We work with associations and other organizations to eradicate these</p>
  </div>
  <div class="feat row2" style="left:780px;top:3239px;height:292px">
    <svg class="ico" viewBox="0 0 78 78"><rect x="12" y="30" width="46" height="24" rx="10" fill="none" stroke="#1d5fb0" stroke-width="5"/><path d="M62 10v36" stroke="#1d5fb0" stroke-width="5"/></svg>
    <h4 style="color:#1f2328">Water Trampoline<br>Management</h4>
    <p>From installation at the start of the season to removal at the end of the season to winter storage, we've got you covered with this service.</p>
  </div>

  <!-- faq -->
  <h2 class="faq-title">FAQs</h2>
  <div class="faq-item open" style="top:3699px">
    <span>How early do lake weeds start to grow?</span>
    <p>Curly-leaf pondweed is one of the first plants to grow in early spring (and typically dies off the quickest at the end of the summer). This is heavily dependent on sunlight, how fast the water warms up, and sediment type (sand versus muck).</p>
    <span class="chev"><svg width="10" height="10" viewBox="0 0 10 10"><path d="M1 3l4 4 4-4" fill="none" stroke="#fff" stroke-width="2"/></svg></span>
  </div>
  <div class="faq-item" style="top:3824px"><span>How fast do lake weeds grow?</span><span class="chev"><svg width="10" height="10" viewBox="0 0 10 10"><path d="M7 1L3 5l4 4" fill="none" stroke="#fff" stroke-width="2"/></svg></span></div>
  <div class="faq-item" style="top:3871px"><span>How big of an area can I treat?</span><span class="chev"><svg width="10" height="10" viewBox="0 0 10 10"><path d="M7 1L3 5l4 4" fill="none" stroke="#fff" stroke-width="2"/></svg></span></div>
  <div class="faq-item" style="top:3918px"><span>What if the treatment area encroaches your neighbor's shoreline?</span><span class="chev"><svg width="10" height="10" viewBox="0 0 10 10"><path d="M7 1L3 5l4 4" fill="none" stroke="#fff" stroke-width="2"/></svg></span></div>
  <div class="faq-item" style="top:3964px"><span>How long does each treatment last?</span><span class="chev"><svg width="10" height="10" viewBox="0 0 10 10"><path d="M7 1L3 5l4 4" fill="none" stroke="#fff" stroke-width="2"/></svg></span></div>
  <div class="faq-item" style="top:4010px"><span>I DO NOT have a natural beach. Can I install one?</span><span class="chev"><svg width="10" height="10" viewBox="0 0 10 10"><path d="M7 1L3 5l4 4" fill="none" stroke="#fff" stroke-width="2"/></svg></span></div>
  <div class="pager"><span class="on">1</span><span>2</span><span>3</span><span>4</span><span>&gt;&gt;</span></div>
  <div class="faq-photo" role="img" aria-label="Boat lift with canopy on a trailer in front of a blue lake"></div>

  <!-- footer -->
  <svg class="footer-wave" width="1200" height="80" viewBox="0 0 1200 80" preserveAspectRatio="none"><path d="M0 30C160 -5 300 10 470 40S820 85 1000 35C1090 10 1160 5 1200 14V80H0z" fill="#222325"/></svg>
  <div class="footer"></div>
  <div class="brand on-dark" style="left:84px;top:4428px">
    <span class="brand-mark"></span>
    <span class="brand-name">Ferncrest</span>
  </div>
  <div class="follow">Follow us</div>
  <div class="socials"><span></span><span></span><span></span><span></span></div>

  <div class="f-head" style="left:403px;top:4410px">Quick Link</div>
  <ul class="f-links"><li>Home</li><li>About Us</li><li>Services</li><li>FAQs</li><li>Contact Us</li></ul>

  <div class="f-head" style="left:552px;top:4406px">Contact info</div>
  <div class="f-info" style="top:4466px">
    <svg width="14" height="16" viewBox="0 0 24 28"><path d="M12 0a9 9 0 00-9 9c0 7 9 17 9 17s9-10 9-17a9 9 0 00-9-9zm0 12a3 3 0 110-6 3 3 0 010 6z" fill="#fff"/></svg>
    <div>1174 Cedar Point Rd<br>Shoreview, MN 55126</div>
  </div>
  <div class="f-info" style="top:4540px">
    <div style="display:flex;flex-direction:column;gap:10px"><svg width="14" height="10" viewBox="0 0 24 16"><rect width="24" height="16" fill="#fff"/><path d="M0 0l12 9 12-9" fill="none" stroke="#222" stroke-width="2"/></svg><svg width="12" height="12" viewBox="0 0 24 24"><path fill="#fff" d="M6.6 10.8a15 15 0 006.6 6.6l2.2-2.2c.3-.3.7-.4 1-.2 1.1.4 2.3.6 3.6.6.6 0 1 .4 1 1V20c0 .6-.4 1-1 1A17 17 0 013 4c0-.6.4-1 1-1h3.5c.6 0 1 .4 1 1 0 1.3.2 2.5.6 3.6.1.3 0 .7-.2 1z"/></svg></div>
    <div>info@ferncrestllc.com<br>(555) 014-2290</div>
  </div>

  <div class="f-head" style="left:748px;top:4356px">Quick Contact</div>
  <div class="field" style="left:756px;top:4422px;width:112px;height:35px">Name*</div>
  <div class="field" style="left:882px;top:4422px;width:116px;height:35px">Phone*</div>
  <div class="field" style="left:1011px;top:4422px;width:113px;height:35px">Email*</div>
  <div class="field" style="left:756px;top:4466px;width:368px;height:68px">Message</div>
  <div class="submit">Submit</div>

  <div class="copy">Copyright © 2022 <b>FERNCREST</b>, All Rights Reserved.</div>
</div>
</body>
</html>
```